Australian residential property business needs a business card design

I need a business card design for my new business 'Harbour Estate Ventures'. The business will involve house purchases, land development sites, renovation projects, sub-divisions etc. I will be buying property from motivated vendors and working with property investors. I will deal with a wide range of people working in the residential property market including real estate agents, councils, tradespeople, banks, home owners, etc.

I would like something simple, not flashy, but a little bit unique. The colours should be in line with my logo. The business card needs to be professional. I would like something memorable, but not 'busy' or too bright. Not boring. Modern ok.

Target Market(s)

Home owners looking to sell their property, real estate agents, tradespeople (e.g. plumbers, builders, electricians etc), property investors, local councils, and anyone else involved in the residential property industry

Industry/Entity Type

Business

Contact Information for Business Card

I need to include my business name/logo, my name, my title, a PO Box number/address, a mobile number, and an email address.

Font styles to use
Serif

Requirements
Must have
• My business card details listed above.

```html
<!DOCTYPE html>
<html lang="en">
<head>
<meta charset="utf-8">
<title>Harbour Estate Ventures – Business Card</title>
<link rel="stylesheet" href="https://fonts.googleapis.com/css2?family=Open+Sans:wght@400;600;700&display=swap">
<style>
  :root {
    --bg: #ecebe8;
    --card: #fbfbfa;
    --orange: #f2a81d;
    --orange-deep: #e8951a;
    --green: #1fa94f;
    --rule: #f3c531;
    --ink: #6f6f6f;
    --ink-soft: #8a8a8a;
  }
  * { box-sizing: border-box; margin: 0; padding: 0; }
  html, body {
    width: 1200px; height: 1022px; overflow: hidden;
    background: var(--bg);
    font-family: "Open Sans", Arial, sans-serif;
  }
  .business-card {
    position: absolute;
    left: 75px; top: 211px;
    width: 1050px; height: 600px;
    background: var(--card);
    overflow: hidden;
    box-shadow: 0 6px 24px rgba(0,0,0,0.12);
  }
  .accent-dot {
    position: absolute;
    right: -48px; top: 70px;
    width: 96px; height: 96px;
    border-radius: 50%;
    background: var(--orange);
  }
  .brand {
    position: absolute;
    left: 70px; top: 200px;
    width: 300px;
    display: flex; align-items: center; gap: 16px;
  }
  .brand-mark {
    flex: none;
    width: 46px; height: 46px;
    border-radius: 50%;
    background: var(--orange);
  }
  .brand-name {
    color: var(--orange-deep);
    font-weight: 700;
    font-size: 30px;
    line-height: 1.15;
    text-transform: uppercase;
    letter-spacing: 0.5px;
  }
  .divider-vertical {
    position: absolute;
    left: 395px; top: 60px;
    width: 2px; height: 480px;
    background: var(--rule);
  }
  .person {
    position: absolute;
    right: 120px; top: 120px;
    text-align: right;
  }
  .person-name {
    color: var(--ink);
    font-weight: 700;
    font-size: 40px;
    letter-spacing: 0.5px;
  }
  .person-title {
    color: var(--orange);
    font-size: 18px;
    margin-top: 2px;
  }
  .title-rule {
    position: absolute;
    left: 395px; right: 120px; top: 212px;
    height: 2px;
    background: var(--rule);
  }
  .contact-list {
    position: absolute;
    left: 440px; top: 330px;
    list-style: none;
    color: var(--ink-soft);
    font-size: 19px;
    line-height: 1.6;
  }
  .contact-list li { display: flex; align-items: center; gap: 14px; }
  .contact-list svg { width: 18px; height: 18px; flex: none; }
  .edge-band {
    position: absolute;
    left: 0; right: 0; bottom: 0;
    height: 34px;
    display: flex;
  }
  .edge-band .band-orange { width: 40%; background: var(--orange); }
  .edge-band .band-green { flex: 1; background: var(--green); }
</style>
</head>
<body>
  <main class="business-card">
    <div class="accent-dot"></div>

    <div class="brand">
      <span class="brand-mark"></span>
      <span class="brand-name">Harbour Estate Ventures</span>
    </div>

    <div class="divider-vertical"></div>

    <div class="person">
      <div class="person-name">Daniel Brooks</div>
      <div class="person-title">Owner</div>
    </div>
    <div class="title-rule"></div>

    <ul class="contact-list">
      <li>
        <svg viewBox="0 0 18 18" aria-hidden="true"><rect x="4" y="1" width="10" height="16" rx="2" fill="none" stroke="#f2a81d" stroke-width="1.6"/><circle cx="9" cy="14" r="1" fill="#f2a81d"/></svg>
        +444 1600 2245
      </li>
      <li>
        <svg viewBox="0 0 18 18" aria-hidden="true"><rect x="1.5" y="4" width="15" height="10" rx="1" fill="none" stroke="#f2a81d" stroke-width="1.6"/><path d="M2 5 L9 10 L16 5" fill="none" stroke="#f2a81d" stroke-width="1.6"/></svg>
        info@danielbrooks.com
      </li>
      <li>
        <svg viewBox="0 0 18 18" aria-hidden="true"><path d="M1.5 9 L9 2.5 L16.5 9" fill="none" stroke="#f2a81d" stroke-width="1.8"/><rect x="4.5" y="8.5" width="9" height="7" fill="#f2a81d"/></svg>
        #48-2150 Harbour Rd, Kingsford, NSW 2032
      </li>
    </ul>

    <div class="edge-band">
      <div class="band-orange"></div>
      <div class="band-green"></div>
    </div>
  </main>
</body>
</html>
```